ORVILMA card Technical Architecture

Hello everyone ORVILMA: It is a consulting firm in Architecture and Construction. I require a card duplexing, sober, elegant, classic but not boring. Update 1: Use the following data for the card. Name: Rodrigo Salinas Tomás Quevedo Position: COO Twitter: @orvilmaAT Homepage: orvilma.com home address not include the participation of all thank you.

Target Market(s)

Construction companies, Architects and Consulting Engineers

Industry/Entity Type

Consulting

Contact Information for Business Card

Los campos que debe tener:
Nombre, Cargo, email, homepage y twitter

Font styles to use
Serif
Sans Serif
Other font styles liked:
• Me gustan playfair display, open sans y roboto, pero estoy sujeto a sus propuestas

Requirements
Must have
• Colors: Present combined proposals in white, red, gray and black Update 1: The two names must be clearly differentiated from the two surnames
Nice to have
• They are free to present their best proposals. I will bring them immediate feedback to the extent you can go see their designs. Complete data for card and logo files will give the winner the

```html
<!DOCTYPE html>
<html lang="es">
<head>
<meta charset="utf-8">
<title>ORVILMA — Tarjetas personales</title>
<link rel="stylesheet" href="https://fonts.googleapis.com/css2?family=EB+Garamond:ital,wght@0,400;0,700;1,400&family=Arimo:ital,wght@1,400;1,700&display=swap">
<style>
  :root {
    --board: #4e4e4e;
    --board-shadow: #474747;
    --footer: #333333;
    --ink: #111111;
    --paper: #ffffff;
    --card-black: #000000;
    --panel: #131a1b;
    --brand-red: #e60f14;
    --label: #ffffff;
  }
  * { margin: 0; padding: 0; box-sizing: border-box; }
  html, body { width: 1200px; height: 722px; overflow: hidden; background: var(--board); }
  .board { position: relative; width: 1200px; height: 722px; background: var(--board); font-family: "EB Garamond", Georgia, serif; }
  .card-shadows { position: absolute; inset: 0; }
  .side-label {
    position: absolute; top: 48px;
    font-family: "Arimo", Arial, sans-serif; font-style: italic; font-weight: 700;
    font-size: 19px; color: var(--label);
  }
  .side-label--front { left: 383px; }
  .side-label--back { left: 923px; }

  .card { position: absolute; top: 82px; width: 434px; height: 434px; border-radius: 36px; overflow: hidden; }
  .card--front { left: 62px; background: var(--card-black); }
  .card--back { left: 614px; width: 433px; height: 433px; background: var(--paper); text-align: center; }

  .front-panel {
    position: absolute; left: 16px; top: 72px; width: 418px; height: 295px;
    background: var(--panel);
    display: flex; flex-direction: column; align-items: center; justify-content: center; gap: 26px;
  }
  .brand-square { width: 34px; height: 34px; background: var(--brand-red); }
  .brand-name {
    font-family: "EB Garamond", Georgia, serif; font-weight: 400;
    font-size: 50px; letter-spacing: 14px; color: var(--paper); line-height: 1;
    padding-left: 14px;
  }

  .holder-given {
    position: absolute; top: 88px; left: 0; right: 0;
    font-size: 33px; color: var(--brand-red); font-weight: 400; word-spacing: 22px; line-height: 1;
  }
  .holder-family {
    position: absolute; top: 128px; left: 0; right: 0;
    font-size: 33px; color: var(--brand-red); font-weight: 700; line-height: 1;
  }
  .holder-role {
    position: absolute; top: 178px; left: 0; right: 0;
    font-style: italic; font-size: 26px; color: var(--ink); line-height: 1; letter-spacing: -0.3px;
  }
  .contact-web {
    position: absolute; top: 296px; left: 0; right: 0;
    font-size: 26px; font-weight: 700; color: var(--ink); line-height: 1;
  }
  .contact-social {
    position: absolute; top: 340px; left: 0; right: 0;
    display: flex; align-items: center; justify-content: center; gap: 10px;
    font-size: 24px; font-weight: 700; color: var(--ink); line-height: 1;
  }
  .contact-dot { width: 14px; height: 14px; border-radius: 50%; background: var(--ink); }

  .spec-band { position: absolute; left: 0; top: 592px; width: 1200px; height: 130px; background: var(--footer); }
  .spec-rule { position: absolute; top: 58px; height: 3px; background: var(--label); }
  .spec-rule--left { left: 0; width: 304px; }
  .spec-rule--right { left: 870px; width: 330px; }
  .spec-text {
    position: absolute; left: 349px; top: 28px; width: 504px;
    font-family: "Arimo", Arial, sans-serif; font-style: italic; font-size: 17.5px;
    color: var(--label); line-height: 21px;
  }
  .spec-line { display: block; text-align: justify; text-align-last: justify; white-space: nowrap; }
  .spec-line--spaced { letter-spacing: 6px; word-spacing: 4px; white-space: normal; }
</style>
</head>
<body>
<main class="board">
  <svg class="card-shadows" width="1200" height="722" viewBox="0 0 1200 722" aria-hidden="true">
    <polygon points="496,280 608,280 512,496 496,512" fill="var(--board-shadow)"/>
    <polygon points="1046,280 1172,280 1182,294 1066,496 1046,512" fill="var(--board-shadow)"/>
  </svg>

  <p class="side-label side-label--front">*Anverso</p>
  <p class="side-label side-label--back">*Reverso</p>

  <section class="card card--front" aria-label="Anverso de la tarjeta">
    <div class="front-panel">
      <span class="brand-square" aria-hidden="true"></span>
      <h1 class="brand-name">ORVILMA</h1>
    </div>
  </section>

  <section class="card card--back" aria-label="Reverso de la tarjeta">
    <p class="holder-given">Tomás Rodrigo</p>
    <p class="holder-family">Salinas Quevedo</p>
    <p class="holder-role">Director de Operaciones</p>
    <p class="contact-web">orvilma.com</p>
    <p class="contact-social"><span class="contact-dot" aria-hidden="true"></span>@orvilmaAT</p>
  </section>

  <footer class="spec-band">
    <span class="spec-rule spec-rule--left"></span>
    <span class="spec-rule spec-rule--right"></span>
    <p class="spec-text">
      <span class="spec-line">Tarjetas personales en formato cuadrado y borde redondeado</span>
      <span class="spec-line spec-line--spaced">Medidas 5,08 cm x 5,08 cm</span>
      <span class="spec-line spec-line--spaced">Papel mate y gramaje 250gr</span>
    </p>
  </footer>
</main>
</body>
</html>
```